Flyer Design Project

I am opening a yoga studio called Willowmere Yoga .Pilates. Fitness
and require a flyer that will be letterbox dropped. It will two sided - DL size.100mm × 210mm

The studio will offer Vinyasa Flow Yoga and Mat Pilates classes. We aim to enable people to lead healthier, happier lives through improved strength, flexibility and general well being that regular yoga and pilates practice offers.

We offer group classes, private and semi private sessions in yoga and pilates.

it must have the logo on it- I have uploaded the logo in two versions - not sure what will look the best.

pick up one of the colours from the logo as the background colour.

Side one:
Simple and clean with one side showing logo and address details, website and with simple intro about studio (if it fits)

Location: 1st Floor, 17 Larkspur Parade, Tindale, 3286
phone: 0428 596143
www.willowmeretindale.com.au

OPENING OCTOBER

other side - class descriptions and intro offer for new clients
$20 for 7 days of classes
$99 for 1 month unlimited.

Class descriptions:
Vinyasa Flow yoga: A class that flows from pose to pose integrating breath, alignment, strength and power. All levels are catered for in a warm room heated to around 26 degrees. You will leave feeling inspired, empowered and energised.

Mat Pilates: A strong, challenging class integrating the key principles of pilates: concentration, control, centring, precision, flowing movement and breath. Using the core as a focus to develop these principles you will be hooked on the physical freedom you experience post workout:improved strength, flexibility and vitality that pilates offers.

Private and semi Private tuition available.

Target Market(s)

mainly women, athletic, 35-55 age, middle class, well educated

Industry/Entity Type

Fitness

Requirements
Must have
• 2 pages
the logo

Should not have
• no pics

```html
<!DOCTYPE html>
<html lang="en">
<head>
<meta charset="utf-8">
<title>Willowmere Yoga .Pilates. Fitness — DL Flyer</title>
<link rel="stylesheet" href="https://fonts.googleapis.com/css2?family=PT+Sans:ital,wght@0,400;0,700;1,700&display=swap">
<style>
  :root {
    --board: #5a5a5a;
    --paper: #ffffff;
    --orange: #f0882a;
    --orange-soft: #f7b676;
    --orange-pale: #fde3c8;
    --red: #e3161d;
    --grey: #5c5c5c;
    --ink: #4a4a4a;
    --font: "PT Sans", "Trebuchet MS", sans-serif;
  }
  * { margin: 0; padding: 0; box-sizing: border-box; }
  html, body { width: 1200px; height: 1121px; overflow: hidden; }
  body { background: var(--board); font-family: var(--font); position: relative; }

  .page {
    position: absolute;
    top: 15px;
    width: 545px;
    height: 1090px;
    overflow: hidden;
    border: 1px solid #9a9a9a;
    text-align: center;
  }
  .page--front {
    left: 15px;
    background: linear-gradient(to bottom, var(--paper) 0%, var(--paper) 34%, var(--orange-pale) 52%, var(--orange-soft) 72%, var(--orange) 90%);
  }
  .page--back {
    left: 640px;
    background: linear-gradient(to bottom, var(--paper) 0%, var(--paper) 40%, var(--orange-pale) 60%, var(--orange-soft) 78%, var(--orange) 92%);
  }

  .brand { position: absolute; top: 33px; left: 0; width: 100%; }
  .brand__mark {
    display: block; width: 200px; height: 200px; margin: 0 auto;
    border-radius: 50%; background: var(--orange);
  }
  .brand__name {
    margin-top: 28px;
    color: var(--grey);
    font-weight: 700;
    font-size: 40px;
    line-height: 46px;
  }

  .intro {
    position: absolute; top: 400px; left: 0; width: 100%;
    color: var(--red); font-weight: 700; font-size: 24px; line-height: 30.6px;
  }
  .intro p + p { margin-top: 30px; }

  .contact {
    position: absolute; top: 782px; left: 0; width: 100%;
    color: var(--grey); font-weight: 700; font-size: 24px; line-height: 30.6px;
  }

  .wave { position: absolute; left: 0; bottom: 0; width: 545px; height: 170px; display: block; }

  .opening {
    position: absolute; left: 0; width: 100%; top: 988px;
    font-weight: 700; font-size: 60px; line-height: 70px; letter-spacing: -0.5px;
    color: var(--paper);
    -webkit-text-stroke: 3px var(--orange);
    paint-order: stroke fill;
  }

  .offers { position: absolute; top: 0; left: 0; width: 545px; height: 260px; display: block; }
  .offers text { font-family: var(--font); font-weight: 700; font-size: 40px; fill: var(--paper); }

  .classes { position: absolute; top: 262px; left: 0; width: 100%; color: var(--ink); }
  .classes__title { font-style: italic; font-weight: 700; font-size: 25px; color: var(--grey); margin-bottom: 24px; }
  .class__name { font-size: 25px; line-height: 30px; color: var(--ink); }
  .class__text { font-size: 18px; line-height: 24.5px; }
  .class__text + .class__text { margin-top: 20px; }
  .class + .class { margin-top: 30px; }
  .tuition { margin-top: 30px; font-weight: 700; font-size: 23px; color: var(--grey); }
</style>
</head>
<body>

<section class="page page--front">
  <header class="brand">
    <span class="brand__mark"></span>
    <div class="brand__name">Willowmere Yoga<br>.Pilates. Fitness</div>
  </header>

  <div class="intro">
    <p>The studio will offer<br>Vinyasa Flow Yoga and<br>Mat Pilates classes.</p>
    <p>We aim to enable people to lead healthier,<br>happier lives through improved strength,<br>flexibility and general well being<br>that regular yoga and pilates practice offers.</p>
    <p>We offer group classes, private and<br>semi private sessions in yoga and pilates.</p>
  </div>

  <address class="contact" style="font-style:normal">
    1st Floor, 17 Larkspur Parade,<br>Tindale, 3286<br>phone: 0428 596143<br>www.willowmeretindale.com.au
  </address>

  <svg class="wave" viewBox="0 0 545 170" aria-hidden="true">
    <path d="M0 36 C120 12 230 70 340 44 C430 22 500 20 545 26 L545 170 L0 170 Z" fill="#ffffff"/>
  </svg>
  <div class="opening">OPENING OCTOBER</div>
</section>

<section class="page page--back">
  <svg class="offers" viewBox="0 0 545 260" aria-label="Introductory offers">
    <polygon points="0,104 545,-6 545,64 0,174" fill="#f0882a"/>
    <polygon points="0,186 545,76 545,142 0,252" fill="#f0882a"/>
    <text x="272" y="97" text-anchor="middle" transform="rotate(-11.4 272 84)">$20 for 7 days of classes</text>
    <text x="272" y="177" text-anchor="middle" transform="rotate(-11.4 272 164)">$99 for 1 month unlimited</text>
  </svg>

  <div class="classes">
    <h2 class="classes__title">Class descriptions</h2>

    <article class="class">
      <h3 class="class__name" style="font-weight:400">Vinyasa Flow yoga</h3>
      <p class="class__text">A class that flows from pose to pose integrating breath,<br>alignment, strength and power.</p>
      <p class="class__text">All levels are catered for in a warm room<br>heated to around 26 degrees.</p>
      <p class="class__text">You will leave feeling inspired,<br>empowered and energised.</p>
    </article>

    <article class="class">
      <h3 class="class__name" style="font-weight:400">Mat Pilates</h3>
      <p class="class__text">A strong, challenging class integrating<br>the key principles of pilates:<br>concentration, control, centring,<br>precision, flowing movement and breath.</p>
      <p class="class__text">Using the core as a focus to develop these<br>principles you will be hooked on the physical<br>freedom you experience post workout:<br>improved strength, flexibility<br>and vitality that pilates offers.</p>
    </article>

    <p class="tuition">Private and semi Private tuition available.</p>
  </div>

  <svg class="wave" viewBox="0 0 545 170" aria-hidden="true">
    <path d="M0 40 C110 14 220 66 330 46 C430 28 500 22 545 30 L545 170 L0 170 Z" fill="#ffffff"/>
  </svg>
  <div class="opening">OPENING OCTOBER</div>
</section>

</body>
</html>
```